Business card for Eyelash extension salon in Beverly Hills,California USA

We need new business card for our salon in Beverly Hills. The salon name is 'Lumarra' . We would like to have...Business name: Lumarra Name of person: will provide later Address 6128 N.Corbel Ridge Blvd Beverly Hills , CA 90210 Phone: will provide later (Text only) Web: www.lumarrastudio-example.com Pictogrid icon, Friendvale icon follow us for seasonal campaign and news @lumarrastudioexample Design should look elegant, high-end, clean, simple, cohesive with my brand. Please refer my brand board. Business name color will be metallic bronzy color. Im thinking grey background or white background. Thanks

Target Market(s)

25-35. Gender neutral. People who are in Entertainment business industry.
This is High-end Eyelash extension salon in Beverly Hills

Industry/Entity Type

Beauty Salon

Contact Information for Business Card

Business name: Lumarra
Name of person: will provide later
Address 6128 N.Corbel Ridge Blvd Beverly Hills , CA 90210
Phone: will provide later (Text only)
Web: www.lumarrastudio-example.com
Pictogrid icon, Friendvale icon
follow us for seasonal campaign and news @lumarrastudioexample

Requirements
Must have
• Beautiful, elegant, clean and simple look but very attractive and modern
Should not have
• We don't like too clutter, too busy designs.

```html
<!DOCTYPE html>
<html lang="en">
<head>
<meta charset="utf-8">
<title>Lumarra Business Card</title>
<link rel="stylesheet" href="https://fonts.googleapis.com/css2?family=Playfair+Display:wght@400;700&family=Poppins:wght@400;600&display=swap">
<style>
  :root {
    --canvas-bg: #ecebe8;
    --card-grey: #a09e9f;
    --bronze: #8e5f3f;
    --marble-light: #f4f4f4;
    --marble-mid: #e2e2e4;
    --ink: #141414;
    --shadow: rgba(0, 0, 0, 0.18);
  }
  * { box-sizing: border-box; margin: 0; padding: 0; }
  html, body {
    width: 1200px;
    height: 800px;
    overflow: hidden;
    background: var(--canvas-bg);
  }
  .canvas {
    width: 1200px;
    height: 800px;
    display: flex;
    align-items: center;
    justify-content: center;
    gap: 40px;
  }
  .card {
    width: 540px;
    height: 309px;
    position: relative;
    box-shadow: 0 10px 28px var(--shadow);
  }

  /* Front */
  .card-front {
    background: var(--card-grey);
    display: flex;
    flex-direction: column;
    align-items: center;
    justify-content: center;
  }
  .brand-name {
    font-family: "Playfair Display", serif;
    font-weight: 400;
    font-size: 92px;
    line-height: 1;
    color: var(--bronze);
  }
  .brand-location {
    margin-top: 14px;
    font-family: "Poppins", sans-serif;
    font-size: 12px;
    letter-spacing: 0.42em;
    color: var(--bronze);
    text-transform: uppercase;
  }

  /* Back */
  .card-back {
    overflow: hidden;
    color: var(--ink);
    font-family: "Poppins", sans-serif;
  }
  .marble-surface {
    position: absolute;
    inset: 0;
    background:
      radial-gradient(ellipse at 20% 30%, var(--marble-light), transparent 60%),
      radial-gradient(ellipse at 80% 70%, var(--marble-light), transparent 55%),
      linear-gradient(160deg, var(--marble-light), var(--marble-mid) 50%, var(--marble-light));
  }
  .back-content {
    position: relative;
    height: 100%;
    padding: 34px 36px 26px;
    display: flex;
    flex-direction: column;
    align-items: center;
  }
  .person-name {
    font-family: "Playfair Display", serif;
    font-weight: 700;
    font-size: 24px;
    letter-spacing: 0.04em;
  }
  .contact-row {
    margin-top: 26px;
    width: 100%;
    display: flex;
    align-items: center;
    justify-content: center;
  }
  .contact-block {
    flex: 1;
    font-size: 13px;
    line-height: 1.5;
  }
  .contact-block.primary { text-align: left; padding-right: 24px; }
  .contact-block.address { text-align: left; padding-left: 24px; }
  .divider {
    width: 1.5px;
    height: 66px;
    background: var(--ink);
  }
  .follow-line {
    margin-top: 28px;
    font-weight: 600;
    font-size: 13px;
  }
  .social-row {
    margin-top: 8px;
    display: flex;
    align-items: center;
    gap: 16px;
    font-size: 13px;
  }
  .social-item {
    display: flex;
    align-items: center;
    gap: 6px;
  }
  .social-dot {
    width: 18px;
    height: 18px;
    border-radius: 50%;
    background: var(--ink);
  }
</style>
</head>
<body>
  <main class="canvas">
    <section class="card card-front" aria-label="Card front">
      <h1 class="brand-name">Lumarra</h1>
      <p class="brand-location">Beverly Hills</p>
    </section>

    <section class="card card-back" aria-label="Card back">
      <div class="marble-surface" role="img" aria-label="White marble texture background"></div>
      <div class="back-content">
        <h2 class="person-name">JOHNATHAN DOE</h2>
        <div class="contact-row">
          <div class="contact-block primary">
            <p>123 456 7890 (Text only)</p>
            <p>www.lumarrastudio-example.com</p>
          </div>
          <span class="divider"></span>
          <div class="contact-block address">
            <p>6128 N.Corbel Ridge Blvd,</p>
            <p>Beverly Hills , CA 90210</p>
          </div>
        </div>
        <p class="follow-line">Follow us for seasonal campaign and news</p>
        <div class="social-row">
          <span class="social-item"><span class="social-dot"></span>Friendvale</span>
          <span class="social-handle">@lumarrastudioexample</span>
          <span class="social-item">Pictogrid<span class="social-dot"></span></span>
        </div>
      </div>
    </section>
  </main>
</body>
</html>
```